Contest - label design for a health related product with 4 color variations

Nuvera-Store (http://www.nuvera-store.example) is an online shop selling health related products and nutritional supplements, such as algae products, wheat grass and barley grass powder. These products have a positive impact on a person's health. Through Craft Huddle, we have designed already a logo for the shop and now we need to create labels that will be placed on a brown glass bottle (see attachment). The logo shall be used without the slogan 'One life. Live it healthy.' when creating the label.

Your job is to design a label with 4 color variations, blue, green, red and yellow. The measurements of the label is 80 mm x 173 mm, but please add 3 mm bleed to each side.

The information that has to go on the label can be taken from the attachment 'label information.pdf'. For the sake of communication, we will divide the label into 3 parts

- left
- middle
- right

The left part and the right part are fixed as this contains legal information. Please use easy to read fonts, non-serifed fonts, such as Arial, Verdana, Calibri. The left part contains a table and if Illustrator provides the possibility for tables, please use it as we need to be able to easily add and remove rows of the table.

The middle part contains the product description, the product quantity (i.e. 100 g), our logo without the slogan 'One live. Live it healthy.' and logos indicating the organic quality of the product (please see attachments). For the product name (i.e. QUB-Tangen) and the quantity (i.e. 100 Tabletten, 200 g) use the attached Lato font. Please note that the vertical position of our logo, the product name and the organic logos has NOT been set yet. You are free to position them where ever you feel in the middle part of the label.

Target Market(s)

Health concious people between 25 and 70

Industry/Entity Type

Health

Requirements
Must have
• - the attached logo without the slogan "One life...."
- the following attributes: healthy, joyful, vivid, lively, abstract, minimalistic
- colors that go along with our logo and the website www.nuvera-store.example
- all fonts need to be editable and not rendered
- the left part should have an editable table where we can add rows if necessary
- the attached font for product name and quantity
- 3 mm bleed on each side, so the final design is 6 mm wider and higher
- the final design will be in editable Illustrator files of a recent version.
Should not have
• - many overlaying, confusing lines or layers
- dark colors
- heavy appearance

```html
<!DOCTYPE html>
<html lang="de">
<head>
<meta charset="utf-8">
<title>QUB-Tangen Etikett</title>
<link href="https://fonts.googleapis.com/css2?family=Lato:wght@400;700;900&family=Arimo:wght@400;700&display=swap" rel="stylesheet">
<style>
  :root {
    --yellow: #ffe800;
    --green: #2f9a3c;
    --leaf: #8ec63f;
    --text: #2b2b2b;
    --paper: #ffffff;
    --line: #c9c9c9;
  }
  html, body { margin: 0; padding: 0; overflow: hidden; background: var(--paper); }
  .label {
    position: relative; width: 1200px; height: 566px; overflow: hidden;
    font-family: "Arimo", Arial, sans-serif; color: var(--text);
  }
  .label-backdrop { position: absolute; inset: 0; }
  .panel { position: absolute; font-size: 12px; line-height: 20px; }
  .panel h3 { margin: 0; font-size: 12px; font-weight: 700; }
  .panel p { margin: 0; }

  /* left: legal panel */
  .legal { left: 34px; top: 74px; width: 400px; }
  .legal .block { margin-bottom: 14px; }
  .nutrition { border-collapse: collapse; font-size: 12px; line-height: 20px; }
  .nutrition th, .nutrition td { padding: 0; text-align: left; font-weight: 400; }
  .nutrition th { font-weight: 700; }
  .nutrition .col-name { width: 110px; }
  .nutrition .col-portion { width: 80px; }

  /* middle: product */
  .product { left: 444px; top: 62px; width: 400px; height: 420px; text-align: center; }
  .product-name {
    margin: 0; font-family: "Lato", sans-serif; font-weight: 900;
    font-size: 36px; line-height: 42px; color: var(--green);
  }
  .product-quantity {
    margin: 2px 0 0; font-family: "Lato", sans-serif; font-size: 13px; color: var(--text);
  }
  .shop-mark {
    position: absolute; left: 0; right: 0; top: 248px;
    display: flex; justify-content: center; align-items: center; gap: 10px;
    font-family: "Arimo", Arial, sans-serif; font-size: 26px; font-weight: 700; color: var(--green);
  }
  .shop-mark .dot { width: 20px; height: 20px; border-radius: 50%; background: var(--yellow); }
  .organic-badges {
    position: absolute; top: 292px; left: 0; right: 0;
    display: flex; justify-content: center; gap: 14px;
  }
  .badge { width: 86px; height: 70px; }
  .badge-round { background: var(--paper); border: 2px solid var(--line); border-radius: 8px; box-sizing: border-box; }
  .badge-leaf { background: var(--leaf); width: 90px; }

  /* right: usage panel */
  .usage { left: 852px; top: 20px; width: 322px; }
  .usage .block { margin-bottom: 12px; }
  .usage ul { margin: 0; padding: 0; list-style: none; }
  .usage li::before { content: "- "; }
</style>
</head>
<body>
<div class="label">
  <svg class="label-backdrop" width="1200" height="566" viewBox="0 0 1200 566" aria-hidden="true">
    <defs>
      <linearGradient id="middle-shade" x1="0" y1="1" x2="0.6" y2="0">
        <stop offset="0" stop-color="#cfcfcf"/>
        <stop offset="0.45" stop-color="#f2f2f2"/>
        <stop offset="1" stop-color="#ffffff"/>
      </linearGradient>
    </defs>
    <rect x="444" y="0" width="420" height="566" fill="url(#middle-shade)"/>
    <path d="M444 0 H830 C720 10 560 40 490 96 C470 60 455 25 444 0 Z" fill="var(--yellow)"/>
    <path d="M446 566 C458 380 458 180 446 0" fill="none" stroke="var(--line)" stroke-width="2"/>
    <path d="M812 0 C842 180 842 400 812 566 H1200 V0 Z" fill="var(--paper)"/>
    <path d="M828 0 C858 180 858 400 828 566 H1200 V0 Z" fill="var(--yellow)"/>
  </svg>

  <section class="panel legal">
    <div class="block">
      <h3>Zutaten</h3>
      <p>QUB-Tangen (QUB - Aphanizomenon Flos Aqua) aus dem<br>Klamath Lake, bei 37° Celsius getrocknet.</p>
    </div>
    <table class="nutrition block">
      <tr><th class="col-name">Nährwertangaben</th><th class="col-portion">in 100 g</th><th>pro Kapsel</th></tr>
      <tr><td>Kohlenhydrate</td><td></td><td></td></tr>
      <tr><td>Fett</td><td></td><td></td></tr>
      <tr><td>Eiweiß</td><td></td><td></td></tr>
      <tr><td colspan="3">Brennwert (kJ / kcal)</td></tr>
    </table>
    <table class="nutrition block" style="margin-top:14px">
      <tr><th class="col-name">Inhaltsstoffe</th><th class="col-portion">pro Kapsel</th><th>% RDA</th></tr>
      <tr><td>Vitamin C</td><td>50,2 mg</td><td>50%</td></tr>
    </table>
    <div class="block" style="margin-top:14px">
      <h3>Vertrieb</h3>
      <p>Marlow Pike Limited<br>Lindenhof-Gasse 12-14<br>1220 Wien<br>Österreich</p>
    </div>
  </section>

  <section class="panel product">
    <h1 class="product-name">QUB-Tangen</h1>
    <p class="product-quantity">100 Tabletten, 200 g</p>
    <div class="shop-mark"><span class="dot"></span>Nuvera-Store</div>
    <div class="organic-badges">
      <div class="badge badge-round" role="img" aria-label="Bio-Siegel"></div>
      <div class="badge badge-leaf" role="img" aria-label="EU-Bio-Siegel"></div>
    </div>
  </section>

  <section class="panel usage">
    <div class="block">
      <h3>Verzehrempfehlung</h3>
      <p style="margin-top:8px">3 x täglich 3 – 5 Tabletten unzerkaut mit Wasser zu den Mahlzeiten einnehmen.</p>
    </div>
    <div class="block">
      <h3>Hinweise</h3>
      <ul style="margin-top:8px">
        <li>Die angegebene tägliche Verzehrmenge sollte nicht überschritten werden.</li>
        <li>Nahrungsergänzungsmittel sind kein Ersatz für eine ausgewogene und abwechslungsreiche Ernährung.</li>
        <li>Das Produkt lichtgeschützt, verschlossen und außerhalb der Reichweite von kleinen Kindern aufbewahren.</li>
        <li>Während der Schwangerschaft und Stillzeiten sollte vor dem Verzehr von Nahrungsergänzungsmitteln ein Arzt konsultiert werden.</li>
      </ul>
    </div>
    <div class="block">
      <h3>Mindesthaltbarkeitsdatum</h3>
      <p>Siehe Boden.</p>
    </div>
  </section>
</div>
</body>
</html>
```